Business Card Design

We sell fish products to corporate food companies who then turn these products into final food products for consumers

Industry/Entity Type

Business

Contact Information for Business Card

I need a corporate business card template for a fish products business. We would like it be professional for use in dealing with multi national companies. This company business card template will be used by multiple employees so the following fields must be open to edit (Name, Phone Number and Email address)

```html
<!DOCTYPE html>
<html lang="en">
<head>
<meta charset="utf-8">
<title>Tidewell Seafoods – Business Card Design #1</title>
<link href="https://fonts.googleapis.com/css2?family=Questrial&family=Tinos&family=Arimo&display=swap" rel="stylesheet">
<style>
  :root {
    --page: #ffffff;
    --frame: #c6e0c9;
    --stage: #e6e6e6;
    --brand-blue: #3a5dab;
    --brand-green: #7dbd8a;
    --fin-green: #cfe6d6;
    --ink: #1e1e1e;
    --card: #ffffff;
  }
  * { margin: 0; padding: 0; box-sizing: border-box; }
  html, body { width: 1200px; height: 900px; overflow: hidden; background: var(--page); }
  .board { position: relative; width: 1200px; height: 900px; }

  .showcase-frame {
    position: absolute; left: -3px; top: 44px; width: 1095px; height: 584px;
    border: 3px solid var(--frame);
  }
  .showcase-stage {
    position: absolute; left: 0; top: 80px; width: 1048px; height: 494px;
    background: var(--stage);
  }

  .business-card {
    position: absolute; left: 214px; top: 150px; width: 620px; height: 354px;
    background: var(--card);
    box-shadow: 0 8px 24px rgba(0,0,0,0.12);
    overflow: hidden;
  }
  .card-brand {
    position: absolute; left: 0; top: 0; width: 282px; height: 100%;
    display: flex; align-items: center; justify-content: center; gap: 10px;
  }
  .card-brand .brand-dot { width: 16px; height: 16px; border-radius: 50%; background: var(--brand-green); }
  .card-brand .brand-name {
    font-family: "Questrial", sans-serif; font-size: 27px; color: var(--brand-blue);
    line-height: 1.1; text-align: center;
  }
  .card-divider {
    position: absolute; left: 282px; top: 20px; width: 4px; height: 314px;
    background: var(--brand-green);
  }
  .card-decoration {
    position: absolute; right: 0; top: 0; width: 160px; height: 100%;
    background: linear-gradient(180deg, var(--fin-green), #e3f1e7);
  }
  .card-holder {
    position: absolute; left: 320px; top: 80px;
    font-family: "Tinos", serif; font-size: 19px; color: var(--ink);
  }
  .card-contacts {
    position: absolute; left: 320px; top: 230px; list-style: none;
    font-family: "Arimo", sans-serif; font-size: 15px; color: var(--ink);
  }
  .card-contacts li { display: flex; align-items: center; gap: 8px; margin-bottom: 8px; }
  .contact-icon { width: 26px; height: 26px; }

  .board-brand {
    position: absolute; left: 120px; top: 740px;
    display: flex; align-items: center; gap: 14px;
  }
  .board-brand .brand-dot { width: 26px; height: 26px; border-radius: 50%; background: var(--brand-blue); }
  .board-brand .brand-name {
    font-family: "Questrial", sans-serif; font-size: 34px; color: var(--brand-blue); line-height: 1.15;
  }
  .board-title {
    position: absolute; left: 412px; top: 690px;
    font-family: "Questrial", sans-serif; font-weight: 400; font-size: 84px;
    line-height: 0.92; letter-spacing: 1px; color: var(--brand-blue);
  }
</style>
</head>
<body>
<main class="board">
  <div class="showcase-frame"></div>
  <div class="showcase-stage"></div>

  <article class="business-card">
    <div class="card-brand">
      <span class="brand-dot"></span>
      <span class="brand-name">TIDEWELL<br>SEAFOODS</span>
    </div>
    <div class="card-divider"></div>
    <div class="card-decoration" role="img" aria-label="Large pale green brand decoration along the card's right edge"></div>
    <p class="card-holder">First Name Last Name</p>
    <ul class="card-contacts">
      <li>
        <svg class="contact-icon" viewBox="0 0 26 26" aria-hidden="true">
          <rect width="26" height="26" rx="5" fill="var(--brand-blue)"/>
          <path d="M9 6c1 0 2 3 2 4s-1.5 1.3-1.2 2.2c.6 1.6 1.8 2.9 3.4 3.6.9.3 1.3-1.2 2.2-1.2s3.6 1 3.6 2c0 1.4-1.6 3-3 3C10.8 19.6 6.4 15 6.2 9 6.2 7.6 7.6 6 9 6z" fill="#fff"/>
        </svg>
        <span>014 5550172</span>
      </li>
      <li>
        <svg class="contact-icon" viewBox="0 0 26 26" aria-hidden="true">
          <rect width="26" height="26" rx="5" fill="var(--brand-blue)"/>
          <rect x="5" y="8" width="16" height="11" fill="#fff"/>
          <path d="M5 8l8 6 8-6" fill="none" stroke="var(--brand-blue)" stroke-width="1.6"/>
        </svg>
        <span>yourmail@tidewell.com</span>
      </li>
    </ul>
  </article>

  <div class="board-brand">
    <span class="brand-dot"></span>
    <span class="brand-name">TIDEWELL<br>SEAFOODS</span>
  </div>
  <h1 class="board-title">BUSINESS CARD<br>DESIGN #1</h1>
</main>
</body>
</html>
```